Small consulting business needs a website designed to highlight value and four offerings

My company is a dynamic consulting firm with four Core Offerings: Learning & Evaluation, Program Management, Facilitation & Coaching; Implementation & Transformation. Our mission is to facilitate organizational change and transformation, and to make space for creativity, joy, belonging, and trust. If done successfully, we grow to better understand ourselves, each other, and the work we do together.

I'd like the website to give a feeling of confidence and clarity. I want the colors to match or compliment my logo. I want to have three tabs - Our Clients, Our Services, and Government.

See attached Word document for additional content. My current website is www.BrightHarborGroup.com.

Some websites I'm inspired by:
https://www.ovalmeadowworks.com
https://www.solvantpartnership.com
https://tqrb.org

Some websites of people/groups in my field that I find uninspiring:
http://danaquillby.com
https://www.moorvale.org

Target Market(s)

State and local government agencies, health tech, and corporate HR departments

Industry/Entity Type

public health, aging, government, health tech

Coding

Number of Pages Required

4 page

Font styles to use
Other font styles liked:
• Calibri and Merriweather

Colors
0054AA
0677BA
7BADD7
CADEEF
E8F1F8
00AB8E
00BBA5
67D7C9
C6EFE9
E9F9F6
FFC000
F8CF3A
FAE287
FDF2CF
FEFAEE
F0912C
F2A743
F7CA91
FBE8D2
FDF5EE

Requirements
Must have
• Attached logo and content, water colors few, and photos.
Nice to have
• Real pictures, which I can provide to the chosen designer
Should not have
• AI generated characters or cartoons.

```html
<!DOCTYPE html>
<html lang="en">
<head>
<meta charset="utf-8">
<title>Bright Harbor Collaborative</title>
<link rel="stylesheet" href="https://fonts.googleapis.com/css2?family=Libre+Baskerville:wght@400;700&family=Carlito:wght@400;700&display=swap">
<style>
  :root {
    --cream: #FEFAEE;
    --teal: #00BBA5;
    --teal-dark: #00AB8E;
    --mint: #E9F9F6;
    --blue: #0054AA;
    --blue-mid: #0677BA;
    --royal: #2A5C9A;
    --gold: #D4A62A;
    --orange: #F0912C;
    --rust: #C8782E;
    --green: #7BAA3F;
    --ink: #141414;
    --rule: #E4E4E4;
    --serif: "Libre Baskerville", Georgia, serif;
    --sans: "Carlito", "Calibri", Arial, sans-serif;
  }
  * { box-sizing: border-box; margin: 0; padding: 0; }
  html, body { width: 1200px; height: 3288px; overflow: hidden; }
  body { position: relative; background: var(--cream); font-family: var(--sans); color: var(--ink); }
  .abs { position: absolute; }

  /* header */
  .site-header { position: absolute; left: 0; top: 0; width: 1200px; height: 87px; border-bottom: 1px solid #E8E2D2; background: var(--cream); }
  .brand { position: absolute; left: 92px; top: 26px; display: flex; align-items: center; gap: 8px; font-family: var(--serif); font-size: 11px; color: var(--ink); line-height: 1.3; }
  .brand-dot { width: 12px; height: 12px; border-radius: 50%; background: var(--gold); }
  .nav { position: absolute; top: 37px; font-size: 11px; color: var(--ink); }
  .nav.active { color: var(--teal); font-weight: 700; }
  .btn { position: absolute; background: var(--orange); color: #fff; font-family: var(--serif); font-size: 11px; font-weight: 700; border-radius: 20px; display: flex; align-items: center; justify-content: center; }

  .down { position: absolute; width: 31px; height: 51px; border: 1.5px solid #333; border-radius: 16px; display: flex; align-items: center; justify-content: center; font-size: 16px; color: #333; }

  /* hero */
  .hero-title { left: 106px; top: 192px; width: 520px; font-family: var(--serif); font-weight: 400; font-size: 39px; line-height: 50px; }
  .hero-text { left: 106px; top: 427px; width: 500px; font-size: 14px; line-height: 19px; }
  .hero-text .name { color: var(--blue-mid); font-weight: 700; }
  .offer-label { font-family: var(--serif); font-size: 19px; text-align: center; line-height: 25px; }
  .offer-art { left: 684px; top: 178px; width: 387px; height: 389px; border-radius: 8px;
    background: linear-gradient(135deg, #2A5C9A 0%, #6C87A8 30%, #D4A62A 50%, #C8782E 68%, #7BAA3F 100%); opacity: .9; }

  /* teal */
  .band-teal { left: 0; top: 674px; width: 1200px; height: 563px; background: var(--teal); color: #fff; }
  .teal-title { font-family: var(--serif); font-weight: 700; font-size: 38px; color: #fff; white-space: nowrap; }
  .teal-rule { position: absolute; height: 1px; background: rgba(255,255,255,.7); }
  .pillar { position: absolute; top: 239px; width: 310px; }
  .pillar h3 { margin-top: 22px; font-family: var(--serif); font-weight: 400; font-size: 25px; }
  .pillar h3 b { font-weight: 700; }
  .pillar p { margin-top: 14px; font-size: 11px; line-height: 19px; }

  /* mint */
  .band-mint { left: 0; top: 1237px; width: 1200px; height: 621px; background: var(--mint); }
  .section-title { width: 1200px; left: 0; text-align: center; font-family: var(--serif); font-weight: 700; font-size: 38px; }
  .photo { position: absolute; width: 193px; height: 249px; }
  .cap { position: absolute; font-family: var(--serif); font-weight: 700; font-size: 15px; line-height: 16px; white-space: nowrap; }
  .dot { position: absolute; width: 16px; height: 16px; border-radius: 50%; }

  /* common ground */
  .big-line { left: 0; width: 1200px; text-align: center; font-family: var(--serif); font-weight: 700; font-size: 120px; line-height: 121px; letter-spacing: -1px; white-space: nowrap; }

  /* collaborate */
  .band-white { left: 0; top: 2244px; width: 1200px; height: 469px; background: #fff; }
  .partner { position: absolute; top: 2394px; width: 198px; height: 173px; border-left: 1px solid var(--rule); padding: 19px 0 0 20px; }
  .partner.last { border-right: 1px solid var(--rule); }
  .partner p { margin-top: 20px; font-family: var(--serif); font-size: 15px; line-height: 19px; }

  /* why us */
  .band-photo { left: 0; top: 2713px; width: 1200px; height: 514px; background: linear-gradient(160deg, #DCE3E8 0%, #B9C3CB 35%, #5F6A74 70%, #2F3842 100%); }
  .why { left: 106px; top: 2638px; width: 363px; height: 350px; background: var(--blue); color: #fff; padding: 50px 50px 0; }
  .why h2 { font-family: var(--serif); font-weight: 700; font-size: 21px; display: flex; align-items: center; gap: 12px; }
  .why h2::after { content: ""; width: 140px; height: 1px; background: rgba(255,255,255,.8); }
  .why p { margin-top: 18px; font-size: 11.5px; line-height: 19px; }

  .site-footer { left: 0; top: 3227px; width: 1200px; height: 61px; background: var(--teal-dark); color: #fff; font-family: var(--serif); font-size: 10px; display: flex; align-items: center; justify-content: center; }
</style>
</head>
<body>

<header class="site-header">
  <div class="brand"><span class="brand-dot"></span><span>Bright Harbor<br>Collaborative</span></div>
  <span class="nav active" style="left:670px">Home</span>
  <span class="nav" style="left:723px">Our Story</span>
  <span class="nav" style="left:793px">Meet Our Partners</span>
  <span class="nav" style="left:904px">Why Us</span>
  <span class="btn" style="left:967px;top:25px;width:124px;height:36px;">Contact Us</span>
</header>

<!-- hero -->
<h1 class="abs hero-title">A seat at the table for<br>collaboration, learning,<br>and meaningful<br>change</h1>
<p class="abs hero-text"><span class="name">Bright Harbor collaborative</span> is a dynamic consulting<br>firm with four core offerings: learning &amp; evaluation, program management,<br>facilitation &amp; coaching; implementation &amp; transformation</p>
<span class="btn" style="left:106px;top:515px;width:124px;height:36px;">Contact Us</span>
<div class="down" style="left:584px;top:575px">↓</div>

<div class="abs offer-art" role="img" aria-label="Illustration of the four core offerings in blue, gold, orange and green"></div>
<div class="abs offer-label" style="left:669px;top:134px;width:120px">Learning</div>
<div class="abs offer-label" style="left:938px;top:134px;width:160px">Implementation</div>
<div class="abs offer-label" style="left:663px;top:585px;width:140px">Facilitation</div>
<div class="abs offer-label" style="left:939px;top:572px;width:160px">Program<br>Management</div>

<!-- teal band -->
<section class="abs band-teal">
  <div class="abs teal-title" style="left:346px;top:74px">Here for you and</div>
  <div class="teal-rule" style="left:715px;top:101px;width:275px"></div>
  <div class="abs teal-title" style="left:535px;top:118px">your team.</div>
  <div class="teal-rule" style="left:211px;top:147px;width:272px"></div>

  <div class="pillar" style="left:106px">
    <svg width="38" height="38" viewBox="0 0 38 38" fill="none" stroke="#fff" stroke-width="1.6"><circle cx="18" cy="20" r="16"/><circle cx="18" cy="20" r="10"/><circle cx="18" cy="20" r="4"/><path d="M18 20 L33 5 M28 5 h5 v5"/></svg>
    <h3>Our <b>mission</b></h3>
    <p>Our mission is to facilitate organizational change and transformation, and to make space for creativity, joy, belonging, and trust. if done successfully, we grow to better understand ourselves, each other, and the work we do together.</p>
  </div>
  <div class="pillar" style="left:443px">
    <svg width="40" height="38" viewBox="0 0 40 38" fill="none" stroke="#fff" stroke-width="1.6"><path d="M2 10V2h8M30 2h8v8M2 28v8h8M30 36h8v-8"/><path d="M6 19 Q20 6 34 19 Q20 32 6 19Z"/><circle cx="20" cy="19" r="5"/></svg>
    <h3>Our <b>vision</b></h3>
    <p>Our vision is to be part of a world where organizations and collaborators connect as human beings first. we envision a future where partners and colleagues strive for ongoing growth together.</p>
  </div>
  <div class="pillar" style="left:781px">
    <svg width="36" height="38" viewBox="0 0 36 38" fill="none" stroke="#fff" stroke-width="1.6"><path d="M4 16 L10 9 H26 L32 16 L18 35 Z M4 16 H32 M10 9 L18 35 L26 9"/><path d="M18 2v4M9 3l2 3M27 3l-2 3"/></svg>
    <h3>Our <b>value</b></h3>
    <p>We are the tranquility in chaos. the steady partner always at the table with you. we drive meaningful and measurable change, resulting in sustained progress towards key community outcomes and multi-sector initiatives. our work produces values realignment, critical technical assistance, and develops strategic plans for innovative organizations ready to elevate their work.</p>
  </div>
</section>

<!-- mint band -->
<section class="abs band-mint">
  <div class="abs section-title" style="top:73px">We help your team...</div>
</section>
<div class="down" style="left:1078px;top:1213px">↓</div>
<div class="abs" role="img" aria-label="Watercolor burst ornament in orange, green and teal" style="left:0;top:1130px;width:255px;height:242px;border-radius:50%;background:radial-gradient(circle,#FFFFFF 0 22%,#F2A743 40%,#7BAA3F 62%,#1F6F6A 80%,transparent 82%)"></div>

<div class="cap" style="left:80px;top:1495px;width:200px;text-align:right">Turn bold visions into<br>practical results.</div>
<span class="dot" style="left:261px;top:1532px;background:var(--blue)"></span>
<div class="cap" style="left:279px;top:1432px;width:200px;text-align:right">Transform conflict into<br>opportunity.</div>
<span class="dot" style="left:461px;top:1469px;background:var(--gold)"></span>
<div class="cap" style="left:721px;top:1432px;width:200px">Strengthen<br>community-led systems.</div>
<span class="dot" style="left:722px;top:1469px;background:var(--rust)"></span>
<div class="cap" style="left:920px;top:1495px;width:150px">Foster a sense of<br>belonging...</div>
<span class="dot" style="left:920px;top:1532px;background:var(--green)"></span>

<div class="photo" role="img" aria-label="Photo: colleagues in conversation" style="left:106px;top:1544px;background:linear-gradient(160deg,#6A5D4F,#B8A690 55%,#E7DED2)"></div>
<div class="photo" role="img" aria-label="Photo: smiling woman in a meeting" style="left:305px;top:1481px;background:linear-gradient(160deg,#3B3631,#9A8F83 55%,#E5E2DC)"></div>
<div class="photo" role="img" aria-label="Photo: man shaking hands" style="left:503px;top:1417px;background:linear-gradient(160deg,#8A8A8A,#D9D9D9 55%,#F2F2F2)"></div>
<div class="photo" role="img" aria-label="Photo: handshake across a table" style="left:702px;top:1481px;background:linear-gradient(160deg,#6E6E6E,#A9A49E 50%,#5E7D9E)"></div>
<div class="photo" role="img" aria-label="Photo: team members greeting" style="left:901px;top:1544px;background:linear-gradient(160deg,#C7B4A0,#7C98B6 50%,#3F5F86)"></div>
<div class="down" style="left:584px;top:1745px">↓</div>

<!-- common ground -->
<div class="abs big-line" style="top:1920px">...Find common</div>
<div class="abs big-line" style="top:2041px">ground.</div>

<!-- collaborate -->
<section class="abs band-white"></section>
<div class="abs" role="img" aria-label="Watercolor circular knot ornament in teal and gold" style="left:36px;top:2143px;width:194px;height:204px;border-radius:50%;background:radial-gradient(circle,#FFFFFF 0 18%,#F8CF3A 38%,#2E8F86 62%,#1C4F5E 82%)"></div>
<div class="down" style="left:1078px;top:2213px;background:#fff">↓</div>
<div class="abs section-title" style="top:2315px">We collaborate with</div>

<div>
  <div class="partner" style="left:106px">
    <svg width="42" height="44" viewBox="0 0 42 44" fill="none" stroke="var(--teal)" stroke-width="1.6"><path d="M21 6 L36 14 V30 L21 38 L6 30 V14 Z M6 14 L21 22 L36 14 M21 22 V38"/><path d="M4 4 l4 4 M38 4 l-4 4" stroke="var(--orange)"/></svg>
    <p>Large-scale<br>companies</p>
  </div>
  <div class="partner" style="left:304px">
    <svg width="42" height="44" viewBox="0 0 42 44" fill="none" stroke="var(--teal)" stroke-width="1.6"><path d="M4 8 V26 L12 36 V42 M38 8 V26 L30 36 V42 M10 14 V26 L16 32 M32 14 V26 L26 32"/><path d="M21 20 C17 15 13 11 17 8 C19 7 21 9 21 10 C21 9 23 7 25 8 C29 11 25 15 21 20Z" stroke="var(--orange)"/></svg>
    <p>National and local<br>nonprofits</p>
  </div>
  <div class="partner" style="left:502px">
    <svg width="42" height="44" viewBox="0 0 42 44" fill="none" stroke="var(--teal)" stroke-width="1.6"><path d="M21 3 V8 M12 17 C12 10 30 10 30 17 Z M8 17 H34 V21 H8 Z M11 21 V33 M17 21 V33 M25 21 V33 M31 21 V33 M6 33 H36 V37 H6 Z M3 40 H39"/></svg>
    <p>State government<br>agencies</p>
  </div>
  <div class="partner" style="left:700px">
    <svg width="42" height="44" viewBox="0 0 42 44" fill="none" stroke="var(--teal)" stroke-width="1.6"><circle cx="21" cy="13" r="10"/><path d="M11 13 H31 M21 3 C16 8 16 18 21 23 C26 18 26 8 21 3"/><path d="M3 30 L12 26 L22 30 L30 27 L39 31 M10 34 L18 38 L24 36" stroke="var(--orange)"/></svg>
    <p>International<br>partnerships &amp;<br>organizations<br>foundations</p>
  </div>
  <div class="partner last" style="left:898px">
    <svg width="42" height="44" viewBox="0 0 42 44" fill="none" stroke="var(--teal)" stroke-width="1.6"><path d="M21 4 L38 13 V31 L21 40 L4 31 V13 Z M4 13 L21 22 L38 13 M21 22 V40"/><path d="M10 20 h6 v6 M26 20 h6 M26 28 h6" stroke="var(--orange)"/></svg>
    <p>Tribal serving-<br>organizations startups<br>in tech</p>
  </div>
</div>
<span class="btn" style="left:538px;top:2601px;width:125px;height:37px;">Contact Us</span>

<!-- why us -->
<section class="abs band-photo" role="img" aria-label="Photo: team meeting around a conference table"></section>
<div class="abs" role="img" aria-label="Watercolor sun and river ornament" style="left:938px;top:2613px;width:198px;height:200px;border-radius:50%;background:linear-gradient(180deg,#F8CF3A 0%,#FAE287 38%,#67D7C9 58%,#1C7A8C 80%,#2B4F6B 100%)"></div>
<div class="abs why">
  <h2>Why Us</h2>
  <p>Through our core offerings and guided by our founder’s traditional and nontraditional methods for engaging and steering a team, we create a sense of belonging, foster transparency, and help to build stronger relationships. our approach helps to drive meaningful change so that organizations and initiatives can clear roadblocks and meet collective goals. our team’s proven ability to transform conflict into opportunity will help to advance your organization and the communities you serve.</p>
</div>

<footer class="abs site-footer">© 2025&nbsp;<b>Bright Harbor Collab.</b>&nbsp;All rights reserved</footer>

</body>
</html>
```